Home inspection business! professional look attracting customers just by looks. Read must haves

its a new business I started on my own for home inspections I would like something very professional to give to real estate agents and clients, its going to have my license number on it my business phone number my name my website as well etc on the back side it will be servicing areas and also what kind of services I offer I also have a business card from someone else the way I would like mine to be. I will attach my logo

Home Inspection

listed in nice to haves

• phone number - 555 293 8471
• website- hollowpinecheck.com
• license number #2938475610
• my name Gavin keropulis
• picture of my logo and me on the front
• on the back of the card. stating I am servicing All of New York and Long Island
• also services I will offer will be home inspection -mold inspection -lead inspection -radon inspection -Termite Inspection -Infared Scan.
• and also we provide inspections for single family homes condos co-ops town-homes
• and commercial property
• same colors as the logos and also if you recommend fonts to look like the logo not sure up to you

```html
<!DOCTYPE html>
<html lang="en">
<head>
<meta charset="utf-8">
<title>Hollow Pine Home Inspectors – Business Card</title>
<link href="https://fonts.googleapis.com/css2?family=Arimo:wght@400;700&display=swap" rel="stylesheet">
<style>
  :root {
    --stage: #2b2b2d;
    --card-white: #f4f4f4;
    --brand-blue: #1479c4;
    --brand-blue-deep: #0e63a6;
    --ink: #2a2a2a;
    --ink-soft: #5a5a5a;
    --on-blue: #ffffff;
  }
  * { box-sizing: border-box; margin: 0; padding: 0; }
  html, body { width: 1200px; height: 997px; overflow: hidden; }
  body {
    background: var(--stage);
    font-family: "Arimo", Arial, sans-serif;
    position: relative;
  }
  .card {
    position: absolute;
    width: 540px;
    height: 310px;
    background: var(--card-white);
    overflow: hidden;
    box-shadow: 0 14px 30px rgba(0,0,0,.45);
  }
  .card-front { left: 60px; top: 130px; }
  .card-back  { left: 600px; top: 540px; }

  /* Front */
  .front-panel {
    position: absolute; inset: 0;
    background: var(--brand-blue);
    clip-path: polygon(48% 0, 100% 0, 100% 100%, 44% 100%);
  }
  .portrait {
    position: absolute;
    left: 300px; top: 20px;
    width: 170px; height: 290px;
    background: linear-gradient(180deg, #e9dcbf 0%, #d9d2c4 22%, #22407a 40%, #1b3568 100%);
    border-radius: 70px 70px 0 0;
    opacity: .9;
  }
  .brand {
    position: absolute;
    left: 24px; top: 136px;
    display: flex; align-items: center; gap: 8px;
  }
  .brand-dot {
    width: 28px; height: 28px; border-radius: 50%;
    background: var(--brand-blue);
    flex: none;
  }
  .brand-name {
    color: var(--ink-soft);
    font-weight: 700;
    font-size: 13px;
    letter-spacing: 1px;
    line-height: 1.3;
    text-transform: uppercase;
  }

  /* Back */
  .back-panel {
    position: absolute; inset: 0;
    background: var(--brand-blue);
    clip-path: polygon(0 0, 63% 0, 60% 100%, 0 100%);
  }
  .services {
    position: absolute;
    left: 26px; top: 20px;
    color: var(--on-blue);
  }
  .services-title {
    font-size: 13px;
    color: var(--ink);
    text-decoration: underline;
    letter-spacing: .5px;
    margin-bottom: 12px;
  }
  .service-list { list-style: none; margin-bottom: 14px; }
  .service-list li {
    font-size: 14px;
    line-height: 18px;
    padding-left: 16px;
    position: relative;
  }
  .service-list li::before {
    content: "";
    position: absolute; left: 2px; top: 5px;
    width: 8px; height: 8px; border-radius: 50%;
    background: var(--on-blue);
  }
  .contact {
    position: absolute;
    right: 20px; top: 46px;
    text-align: right;
  }
  .contact-name {
    color: var(--brand-blue-deep);
    font-weight: 700;
    font-size: 16px;
    letter-spacing: .5px;
    text-transform: uppercase;
  }
  .contact-role {
    color: var(--ink);
    font-size: 12px;
    letter-spacing: .5px;
    margin-bottom: 20px;
  }
  .contact-line {
    display: flex; justify-content: flex-end; align-items: center; gap: 6px;
    color: var(--ink);
    font-size: 13px;
    margin-bottom: 6px;
  }
  .contact-line svg { width: 12px; height: 12px; fill: var(--brand-blue); }
  .contact-license {
    color: var(--ink);
    font-size: 12px;
    margin-top: 10px;
  }
</style>
</head>
<body>

<section class="card card-front" aria-label="Card front">
  <div class="front-panel"></div>
  <div class="portrait" role="img" aria-label="Photo of the inspector in a navy suit holding a straw hat"></div>
  <div class="brand">
    <span class="brand-dot"></span>
    <span class="brand-name">Hollow Pine<br>Home Inspectors</span>
  </div>
</section>

<section class="card card-back" aria-label="Card back">
  <div class="back-panel"></div>
  <div class="services">
    <p class="services-title">WE PROVIDE INSPECTIONS FOR</p>
    <ul class="service-list">
      <li>Co-ops town-homes</li>
      <li>Commercial property</li>
      <li>Single family homes condos</li>
    </ul>
    <ul class="service-list">
      <li>Mold Inspection</li>
      <li>Lead Inspection</li>
      <li>Home Inspection</li>
      <li>Infared Scan.</li>
      <li>Termite Inspect</li>
      <li>Radon Inspection</li>
    </ul>
    <ul class="service-list">
      <li>All of New York<br>&amp; Long Island</li>
    </ul>
  </div>
  <div class="contact">
    <p class="contact-name">Gavin Keropulis</p>
    <p class="contact-role">HOME INSPECTOR</p>
    <p class="contact-line">555 293 8471
      <svg viewBox="0 0 24 24" aria-hidden="true"><path d="M6.6 10.8a15 15 0 0 0 6.6 6.6l2.2-2.2a1 1 0 0 1 1-.25 11.4 11.4 0 0 0 3.6.57 1 1 0 0 1 1 1V20a1 1 0 0 1-1 1A17 17 0 0 1 3 4a1 1 0 0 1 1-1h3.5a1 1 0 0 1 1 1c0 1.25.2 2.45.57 3.57a1 1 0 0 1-.25 1z"/></svg>
    </p>
    <p class="contact-line">www.hollowpinecheck.com
      <svg viewBox="0 0 24 24" aria-hidden="true"><circle cx="12" cy="12" r="10"/></svg>
    </p>
    <p class="contact-license">License #2938475610</p>
  </div>
</section>

</body>
</html>
```